Accommodation business card design

We need a business card designed for our long-term accommodation business based in Australia. The business card must match the style of the attached letterhead and logo. The same contact details that are on the letterhead will also go on the card except that the card must list the contact details in the following order:phone, email, home address, ABN.

The card will be printed on .76mm white pvc plastic (same as credit cards), printed both sides and will be silver foil stamped on at least one side (preferably 2 sides) The design template is attached, but please go to www.zt.com.au for more specs.

The only other addition the card will be my name: Malcolm Darby

```html
<!DOCTYPE html>
<html lang="en">
<head>
<meta charset="utf-8">
<title>Summit Lodging – Business Card</title>
<link rel="stylesheet" href="https://fonts.googleapis.com/css2?family=Dancing+Script:wght@500&family=Open+Sans:wght@400&family=Saira+Condensed:wght@700&display=swap">
<style>
  :root {
    --brown: #8a4b40;
    --maroon: #6b1a3a;
    --white: #ffffff;
    --edge: #6f6f6f;
  }
  html, body {
    margin: 0;
    padding: 0;
    width: 1200px;
    height: 998px;
    overflow: hidden;
    background: var(--white);
  }
  .canvas {
    position: relative;
    width: 1200px;
    height: 998px;
  }
  .card {
    position: absolute;
    top: 251px;
    width: 308px;
    height: 492px;
    border: 1px solid var(--edge);
    border-radius: 22px;
    overflow: hidden;
    background: var(--white);
    box-sizing: border-box;
  }
  .card--front { left: 141px; }
  .card--back { left: 747px; }
  .card__wave {
    position: absolute;
    inset: 0;
    width: 100%;
    height: 100%;
  }
  .wave-body { fill: var(--brown); }
  .wave-accent { fill: var(--maroon); }

  .brand {
    position: absolute;
    left: 18px;
    top: 18px;
    display: flex;
    align-items: center;
    gap: 14px;
  }
  .brand__mark {
    width: 80px;
    height: 84px;
    background: var(--maroon);
  }
  .brand__name {
    font-family: "Saira Condensed", "Arial Narrow", sans-serif;
    font-weight: 700;
    color: var(--brown);
    font-size: 46px;
    line-height: 0.95;
    letter-spacing: 0.5px;
    text-transform: uppercase;
  }
  .brand__name small {
    display: block;
    font-size: 24px;
    letter-spacing: 0.3px;
  }

  .holder-name {
    position: absolute;
    top: 52px;
    left: 0;
    width: 100%;
    text-align: center;
    font-family: "Dancing Script", cursive;
    font-weight: 500;
    font-size: 27px;
    color: var(--maroon);
    margin: 0;
  }

  .contact {
    position: absolute;
    left: 18px;
    top: 212px;
    margin: 0;
    padding: 0;
    list-style: none;
    font-family: "Open Sans", Arial, sans-serif;
    font-size: 16px;
    line-height: 24px;
    color: var(--white);
  }
  .contact__item {
    display: flex;
    align-items: flex-start;
    gap: 5px;
    margin-bottom: 17px;
  }
  .contact__icon {
    flex: none;
    width: 20px;
    height: 20px;
    margin-top: 2px;
  }
  .contact__item--abn {
    padding-left: 25px;
    margin-top: 25px;
  }
</style>
</head>
<body>
<main class="canvas">

  <section class="card card--front" aria-label="Card front">
    <svg class="card__wave" viewBox="0 0 308 492" preserveAspectRatio="none" aria-hidden="true">
      <path class="wave-body" d="M0,120 Q150,165 308,148 L308,492 L0,492 Z"/>
      <path class="wave-accent" d="M73,134 Q200,160 308,114 L308,142 Q200,156 73,134 Z"/>
    </svg>
    <div class="brand">
      <div class="brand__mark"></div>
      <div class="brand__name">Summit<small>Lodging</small></div>
    </div>
  </section>

  <section class="card card--back" aria-label="Card back">
    <svg class="card__wave" viewBox="0 0 308 492" preserveAspectRatio="none" aria-hidden="true">
      <path class="wave-body" d="M0,120 Q150,165 308,148 L308,492 L0,492 Z"/>
      <path class="wave-accent" d="M73,134 Q200,160 308,114 L308,142 Q200,156 73,134 Z"/>
    </svg>
    <p class="holder-name">Malcolm Darby</p>
    <ul class="contact">
      <li class="contact__item">
        <svg class="contact__icon" viewBox="0 0 20 20" aria-hidden="true">
          <circle cx="10" cy="10" r="10" fill="#fff"/>
          <path d="M7 4.5 L9 7.5 L7.8 8.8 Q9 11.5 11.2 12.2 L12.5 11 L15.5 13 L14 15.5 Q8 15 4.8 7 Z" fill="#8a4b40"/>
        </svg>
        <span>0400 555 218</span>
      </li>
      <li class="contact__item">
        <svg class="contact__icon" viewBox="0 0 20 20" aria-hidden="true">
          <circle cx="10" cy="10" r="10" fill="#fff"/>
          <rect x="4.5" y="6.5" width="11" height="7.5" fill="none" stroke="#8a4b40" stroke-width="1.3"/>
          <path d="M4.5 6.5 L10 11 L15.5 6.5" fill="none" stroke="#8a4b40" stroke-width="1.3"/>
        </svg>
        <span>malcolm.darby@example.com</span>
      </li>
      <li class="contact__item">
        <svg class="contact__icon" viewBox="0 0 20 20" aria-hidden="true">
          <circle cx="10" cy="10" r="10" fill="#fff"/>
          <path d="M4 10 L10 4.5 L16 10 L14.5 10 L14.5 15 L5.5 15 L5.5 10 Z" fill="#8a4b40"/>
          <rect x="8.7" y="11" width="2.6" height="4" fill="#fff"/>
        </svg>
        <span>PO Box 1180, Ridgeway Mail Centre<br>QLD 4700</span>
      </li>
      <li class="contact__item contact__item--abn">
        <span>ABN 12 345 678 901</span>
      </li>
    </ul>
  </section>

</main>
</body>
</html>
```